Info Graphic about Maple Ridge Restaurant

This info graphic should detail all releavent details about Maple Ridge, such as opening hours, accepted payment methods, home delivery areas etc. please refer attached word document for details.

Also attached a pdf with old info graphic.

IMPORTANT:. Given there is lot of text, I expect the designer to make this interesting. This will be printed in A1 and also A4
Also, I need this in both Portrait and landscape designs.

Industry/Entity Type

Hospitality

Font styles to use
Serif
Sans Serif
Decorative
Script
Other font styles liked:
• I let designer choose

Colors

Designer to choose colors to be used in the design.

Requirements
Must have
• Refer attached word doc
Nice to have
• Refer attached word doc
Should not have
• Refer attached word doc

```html
<!DOCTYPE html>
<html lang="en">
<head>
<meta charset="utf-8">
<title>Maple Ridge Indian Restaurant – Info Sheet</title>
<link href="https://fonts.googleapis.com/css2?family=Berkshire+Swash&family=Lato:wght@400;700&family=Marcellus+SC&display=swap" rel="stylesheet">
<style>
:root{
  --red:#c1212c;
  --red-bright:#e8222e;
  --maroon:#9e1c22;
  --yellow:#f6b818;
  --orange:#ec6a2a;
  --rust:#c45a26;
  --amber:#d9822b;
  --olive:#c2b73a;
  --olive-dark:#857b32;
  --brown:#6b3a2a;
  --ink:#333;
  --line:#d8d8d8;
  --green:#b7b22c;
  --navy:#1e3a6e;
  --white:#fff;
}
*{margin:0;padding:0;box-sizing:border-box}
html,body{width:848px;height:1200px;overflow:hidden;background:var(--white)}
body{font-family:"Lato",sans-serif;color:var(--ink);position:relative}
.abs{position:absolute}
.sc{font-family:"Marcellus SC",serif}

/* header */
.rope{left:0;top:0;width:848px;height:260px}
.title-banner{left:110px;top:51px;width:628px;height:119px;background:var(--red);display:flex;align-items:center;justify-content:center}
.title-banner h1{font-family:"Berkshire Swash",cursive;color:var(--white);font-weight:400;font-size:40px;letter-spacing:1px}
.url-ribbon{left:144px;top:161px;width:564px;height:60px;background:var(--yellow);clip-path:polygon(0 12%,100% 0,100% 100%,50% 88%,0 100%);display:flex;align-items:center;justify-content:center;color:var(--white);font-size:25px;padding-top:6px}
.chilli-art{top:76px;width:72px;height:94px;border-radius:40% 40% 50% 50%;background:linear-gradient(90deg,#c1212c,#e85a22 45%,#f0b020 80%,#a9b530)}
.chilli-left{left:17px}.chilli-right{left:763px}

/* hours */
.hours{left:28px;top:250px;width:440px;height:204px;border:2px solid var(--ink);display:grid;grid-template-columns:142px 149px 149px;grid-template-rows:129px 37px 38px}
.hours .cell{display:flex;align-items:center;justify-content:center;font-size:14.5px;border-left:1px solid var(--ink)}
.hours .head{flex-direction:column;gap:12px;font-size:16px}
.hours .head svg{width:60px;height:60px}
.hours .open{background:var(--red-bright);color:var(--yellow);border-left:none}
.hours .morning{color:var(--yellow)}
.hours .evening{color:var(--maroon)}
.hours .day{background:#4a4a4a;color:var(--white);border-left:none;border-top:1px solid #777}
.hours .time{border-top:1px solid var(--line)}
.buffet{left:36px;top:466px;font-size:13.5px}

/* vouchers */
.vouchers{left:499px;top:250px;width:321px;height:210px;background:var(--orange);border-radius:26px;overflow:hidden;color:var(--white)}
.vouchers h2{height:51px;background:#c73a26;font-weight:400;font-size:19px;display:flex;align-items:center;justify-content:center}
.vouchers svg{position:absolute;left:30px;top:88px;width:56px;height:90px}
.vouchers p{position:absolute;left:108px;width:205px;font-size:13.5px;line-height:23px}

/* delivery */
.delivery{left:28px;top:518px;width:441px;height:228px}
.delivery-head{height:69px;background:var(--yellow);display:flex;align-items:center;padding-left:78px;color:var(--maroon);font-size:18px;position:relative}
.delivery-head svg{position:absolute;left:78px;top:8px;width:56px;height:54px}
.delivery-head span{margin-left:72px}
.bookmark{position:absolute;right:20px;top:0;width:22px;height:32px;background:var(--amber);clip-path:polygon(0 0,100% 0,100% 100%,50% 70%,0 100%)}
.suburbs{display:grid;grid-template-columns:repeat(4,110px);grid-auto-rows:40px;border-left:1px solid var(--line)}
.suburbs div{display:flex;align-items:center;padding-left:13px;font-size:15px;border-right:1px solid var(--line);border-bottom:1px solid var(--line)}
.suburbs .charge{grid-column:span 3;background:var(--amber);color:var(--white);padding-left:10px;font-size:15px}

/* payment */
.pay-panel{left:501px;top:488px;width:144px;height:258px;background:var(--red);color:var(--yellow);text-align:center;overflow:hidden}
.pay-panel::before{content:"";position:absolute;left:0;top:0;border-top:32px solid var(--maroon);border-right:32px solid transparent}
.pay-panel::after{content:"";position:absolute;left:0;bottom:0;border-bottom:16px solid var(--maroon);border-right:16px solid transparent}
.pay-panel svg{position:absolute;left:27px;top:30px;width:96px;height:96px}
.pay-panel h3{position:absolute;top:132px;width:100%;font-weight:400;font-size:20px;line-height:28px}
.pay-panel p{position:absolute;top:193px;width:100%;color:var(--white);font-size:13px;line-height:16px}
.pay-table{left:645px;top:488px;width:175px;border-top:1px solid var(--line)}
.pay-table li{list-style:none;height:37px;display:flex;align-items:center;border-bottom:1px solid var(--line);border-right:1px solid var(--line);font-size:14px}
.pay-table li span{flex:1;padding-left:13px;border-right:1px solid var(--line);height:100%;display:flex;align-items:center}
.pay-table li svg{width:63px;height:20px}

/* notices */
.outside{left:28px;top:772px;display:flex;align-items:center;gap:10px;color:var(--red);font-size:18px}
.outside svg{width:42px;height:40px}
.byo{left:376px;top:773px;width:446px;height:96px;border:2px dashed #5a5a5a;background:var(--yellow)}
.byo .dot{position:absolute;left:33px;top:40px;width:12px;height:12px;border-radius:50%;background:#b07a2a}
.byo h3{position:absolute;left:80px;top:22px;font-weight:400;font-size:21px;color:var(--maroon)}
.byo p{position:absolute;left:68px;top:56px;font-size:14px;color:var(--white)}
.byo .glass{position:absolute;right:-10px;top:9px;width:103px;height:68px;background:var(--amber)}
.byo .glass svg{position:absolute;left:32px;top:6px;width:40px;height:56px}

/* booking */
.booking{left:28px;top:835px;width:320px;height:259px;background:var(--rust);border:2px dashed var(--brown);border-radius:28px 28px 0 0;color:var(--white);clip-path:polygon(0 0,100% 0,100% 92%,88% 97%,80% 91%,66% 100%,52% 90%,38% 98%,24% 92%,10% 100%,0 94%)}
.booking .cal{position:absolute;left:122px;top:25px;width:76px;height:72px}
.booking h3{position:absolute;top:112px;width:100%;text-align:center;font-weight:400;font-size:20px}
.contact{position:absolute;left:68px;top:148px;list-style:none;font-size:13.5px;line-height:26px}
.contact li{display:flex;align-items:center;gap:10px;margin-left:-10px}
.contact svg{width:13px;height:13px}

/* services */
.services{left:378px;top:896px;width:442px;height:170px;background:var(--olive);border-radius:30px;overflow:hidden;color:var(--white)}
.services .band{position:absolute;left:42px;top:0;width:131px;height:100%;background:var(--olive-dark);text-align:center}
.services .band h3{margin-top:44px;font-weight:400;font-size:18px}
.services .band svg{margin-top:16px;width:82px;height:60px}
.services ul{position:absolute;left:204px;top:14px;list-style:none;font-size:16.5px;line-height:30px}
.services li::before{content:"•";margin-right:9px;font-size:13px}

/* footer */
.divider{left:0;top:1070px;width:848px;height:40px}
.partners{left:0;top:1120px;width:848px;height:60px;display:flex;align-items:center;justify-content:space-around;color:var(--navy);font-size:40px}
.partner-named{display:flex;align-items:center;gap:8px;font-size:34px}
.partner-named i{width:22px;height:22px;border-radius:50%;background:var(--navy)}
</style>
</head>
<body>

<svg class="abs rope" viewBox="0 0 848 260" aria-hidden="true">
  <path d="M0 36 Q60 44 116 58" stroke="#6b3a2a" stroke-width="5" fill="none"/>
  <path d="M732 58 Q790 44 848 36" stroke="#6b3a2a" stroke-width="5" fill="none"/>
  <path d="M0 238 Q60 180 116 166" stroke="#6b3a2a" stroke-width="5" fill="none"/>
  <path d="M732 166 Q790 180 848 238" stroke="#6b3a2a" stroke-width="5" fill="none"/>
</svg>
<div class="abs chilli-art chilli-left" role="img" aria-label="Illustration of a bunch of red, orange and yellow chillies"></div>
<div class="abs chilli-art chilli-right" role="img" aria-label="Illustration of a bunch of red, orange and yellow chillies"></div>
<div class="abs title-banner"><h1>Maple Ridge Indian Restaurant</h1></div>
<div class="abs url-ribbon">www.mapleridgedining.com.au</div>

<section class="abs hours">
  <div class="cell head open sc">
    <svg viewBox="0 0 60 60"><circle cx="30" cy="30" r="26" fill="none" stroke="#9e1c22" stroke-width="3"/><path d="M20 30l8 8 13-15" fill="none" stroke="#9e1c22" stroke-width="3"/></svg>
    Opening Hours</div>
  <div class="cell head morning sc">
    <svg viewBox="0 0 60 60"><circle cx="30" cy="30" r="12" fill="none" stroke="#f6b818" stroke-width="4"/><g stroke="#f6b818" stroke-width="4" stroke-linecap="round"><path d="M30 4v6M30 50v6M4 30h6M50 30h6M12 12l4 4M44 44l4 4M48 12l-4 4M16 44l-4 4"/></g></svg>
    Morning</div>
  <div class="cell head evening sc">
    <svg viewBox="0 0 60 60"><path d="M36 6A24 24 0 1 0 56 42 20 20 0 1 1 36 6z" fill="#9e1c22"/></svg>
    Evening</div>
  <div class="cell day">Monday to Friday</div>
  <div class="cell time">11:30AM - 2:30PM</div>
  <div class="cell time">5:00PM - 9:00PM</div>
  <div class="cell day">Saturday to Sunday</div>
  <div class="cell time">9.30AM - 2:30PM</div>
  <div class="cell time">5:00PM - 9:00PM</div>
</section>
<p class="abs buffet">*Dinner Buffet is available only from Mon-Thu from 5:30PM-8:30PM</p>

<section class="abs vouchers">
  <h2 class="sc">• Discount Vouchers: •</h2>
  <svg viewBox="0 0 56 90"><path d="M3 3h16a9 7 0 0 0 18 0h16v84H3z" fill="none" stroke="#c1212c" stroke-width="4"/><path d="M3 28h50" stroke="#c1212c" stroke-width="3" stroke-dasharray="5 4"/><circle cx="20" cy="48" r="5" fill="none" stroke="#c1212c" stroke-width="3"/><circle cx="37" cy="64" r="5" fill="none" stroke="#c1212c" stroke-width="3"/><path d="M40 44L16 68" stroke="#c1212c" stroke-width="3"/></svg>
  <p style="top:70px">We accept Dining Pass Book Vouchers and Maple Ridge supplied Discount vouchers.</p>
  <p style="top:146px">Dining Pass Vouchers are eligible only for Dine-In.</p>
</section>

<section class="abs delivery">
  <div class="delivery-head sc">
    <svg viewBox="0 0 56 54"><path d="M4 18l14-6 16 6 16-6v34l-16 6-16-6-14 6z" fill="none" stroke="#fff" stroke-width="3"/><path d="M18 12v34M34 18v34" stroke="#fff" stroke-width="3"/><path d="M10 34q10-8 18 0t18-4" fill="none" stroke="#fff" stroke-width="2" stroke-dasharray="3 3"/><circle cx="46" cy="9" r="6" fill="none" stroke="#fff" stroke-width="3"/></svg>
    <span>Suburbs we Deliver to</span>
    <div class="bookmark"></div>
  </div>
  <div class="suburbs">
    <div>Beldon</div><div>Craigie</div><div>Darch</div><div>Duncraig</div>
    <div>Edgewater</div><div>Greenwood</div><div>Hocking</div><div>Kingsleyt</div>
    <div>Madeley</div><div>Padbury</div><div>Pearsall</div><div>Wangara</div>
    <div>Woodvale</div><div class="charge">Delivery Charges $5 minimum order value $30</div>
  </div>
</section>

<section class="abs pay-panel">
  <svg viewBox="0 0 96 96"><rect x="6" y="30" width="84" height="60" rx="4" fill="none" stroke="#9e1c22" stroke-width="4"/><path d="M16 30l18-22 14 16 10-12 16 18" fill="none" stroke="#9e1c22" stroke-width="4"/><rect x="70" y="52" width="22" height="16" rx="3" fill="none" stroke="#9e1c22" stroke-width="4"/><path d="M14 82h6" stroke="#9e1c22" stroke-width="4"/></svg>
  <h3 class="sc">Payment<br>Methods:</h3>
  <p>* Surcharge of<br>21.8% apply</p>
</section>
<ul class="abs pay-table">
  <li><span>Cash</span><svg viewBox="0 0 63 20"><circle cx="32" cy="10" r="9" fill="#b7b22c"/><path d="M28 10l3 3 5-6" stroke="#fff" stroke-width="2" fill="none"/></svg></li>
  <li><span>Tapline</span><svg viewBox="0 0 63 20"><circle cx="32" cy="10" r="9" fill="#b7b22c"/><path d="M28 10l3 3 5-6" stroke="#fff" stroke-width="2" fill="none"/></svg></li>
  <li><span>Nova/Meridian</span><svg viewBox="0 0 63 20"><circle cx="32" cy="10" r="9" fill="#b7b22c"/><path d="M28 10l3 3 5-6" stroke="#fff" stroke-width="2" fill="none"/></svg></li>
  <li><span>Debit/Credit</span><svg viewBox="0 0 63 20"><circle cx="32" cy="10" r="9" fill="#b7b22c"/><path d="M28 10l3 3 5-6" stroke="#fff" stroke-width="2" fill="none"/></svg></li>
  <li><span>Orbex*</span><svg viewBox="0 0 63 20"><circle cx="32" cy="10" r="9" fill="#b7b22c"/><path d="M28 10l3 3 5-6" stroke="#fff" stroke-width="2" fill="none"/></svg></li>
  <li><span>KDX</span><svg viewBox="0 0 63 20"><circle cx="32" cy="10" r="9" fill="#b7b22c"/><path d="M28 10l3 3 5-6" stroke="#fff" stroke-width="2" fill="none"/></svg></li>
  <li><span>Dinewell</span><svg viewBox="0 0 63 20"><circle cx="32" cy="10" r="9" fill="#e8222e"/><path d="M29 7l6 6M35 7l-6 6" stroke="#fff" stroke-width="2"/></svg></li>
</ul>

<div class="abs outside sc">
  <svg viewBox="0 0 42 40"><path d="M21 3L39 37H3z" fill="none" stroke="#e8222e" stroke-width="3" stroke-linejoin="round"/><path d="M21 14v12" stroke="#e8222e" stroke-width="3"/><circle cx="21" cy="31" r="2" fill="#e8222e"/></svg>
  Outside Food is not allowed
</div>

<section class="abs byo">
  <div class="dot"></div>
  <h3 class="sc">BYO (Bring your own)</h3>
  <p>Wine only - Corkage per bottle apply</p>
  <div class="glass"><svg viewBox="0 0 40 56"><path d="M6 3h28v14a14 14 0 0 1-28 0z" fill="none" stroke="#fff" stroke-width="3.5"/><path d="M6 16h28M20 31v20M10 53h20" stroke="#fff" stroke-width="3.5"/></svg></div>
</section>

<section class="abs booking">
  <svg class="cal" viewBox="0 0 76 72"><rect x="3" y="8" width="70" height="61" rx="5" fill="none" stroke="#8a2a1a" stroke-width="4"/><path d="M3 22h70M20 2v12M56 2v12" stroke="#8a2a1a" stroke-width="4"/><g fill="#8a2a1a"><rect x="14" y="30" width="7" height="6"/><rect x="27" y="30" width="7" height="6"/><rect x="40" y="30" width="7" height="6"/><rect x="53" y="30" width="7" height="6"/><rect x="14" y="42" width="7" height="6"/><rect x="27" y="42" width="7" height="6"/><rect x="40" y="42" width="7" height="6"/><rect x="53" y="42" width="7" height="6"/><rect x="14" y="54" width="7" height="6"/><rect x="27" y="54" width="7" height="6"/></g></svg>
  <h3 class="sc">Bookings/Order Contact</h3>
  <ul class="contact">
    <li><svg viewBox="0 0 13 13"><path d="M3 1l2 3-1 2q1 2 3 3l2-1 3 2-1 2Q6 13 1 3z" fill="#e07a40"/></svg>08 5550 7314</li>
    <li><svg viewBox="0 0 13 13"><rect x="0" y="2" width="13" height="9" fill="#e07a40"/><path d="M0 2l6.5 5L13 2" stroke="#c45a26" fill="none"/></svg>admin@mapleridgedining.com.au</li>
    <li><svg viewBox="0 0 13 13"><circle cx="6.5" cy="6.5" r="5.5" fill="none" stroke="#e07a40" stroke-width="1.5"/><path d="M1 6.5h11M6.5 1v11" stroke="#e07a40"/></svg>www.mapleridgedining.com.au</li>
  </ul>
</section>

<section class="abs services">
  <div class="band">
    <h3 class="sc">Services</h3>
    <svg viewBox="0 0 82 60"><circle cx="41" cy="8" r="4" fill="none" stroke="#fff" stroke-width="3"/><path d="M8 46a33 33 0 0 1 66 0z" fill="none" stroke="#fff" stroke-width="3.5"/><path d="M2 52h78" stroke="#fff" stroke-width="4"/></svg>
  </div>
  <ul>
    <li>Functions/Parties</li>
    <li>Bulk Cooking</li>
    <li>Special Orders</li>
    <li>Business Meetings</li>
    <li>Seminars/Presentations</li>
  </ul>
</section>

<svg class="abs divider" viewBox="0 0 848 40" aria-hidden="true">
  <path d="M0 22l20-6 14 10 20-14 22 12 28-8 30 16 30-14 26 10 28-18 24 16 20-6 34 14 26-12 30 10 24-14 28 16 30-10 24 8 26-14 28 12 24-6 30 14 28-16 26 10 30-8 26 12 28-14 22 10 20-6" fill="none" stroke="#ddd" stroke-width="2"/>
</svg>
<div class="abs partners">
  <span>LOGO1</span>
  <span class="partner-named"><i></i>Harbour Aid</span>
  <span>LOGO3</span>
  <span>LOGO4</span>
</div>

</body>
</html>
```